Varnek Group Business Card

Varnek Group — Business Card Design Brief
Overview
Design a double-sided business card for Varnek Group that highlights our two service arms: Varnek Communications (telecommunications) and Varnek Energy (business energy solutions). The card should feel smart and stand out when handed to clients.

Objectives
Showcase our areas of specialty clearly.
Reflect the overall Varnek / Varnek Group brand while acknowledging both arms.
Explore using both logos (Communications + Energy) or one unified logo, depending on the design.

Deliverables
One double-sided business card design (front + back).

Content & Copy
Front (preferred): Logo: Varnek / Varnek Group
Descriptor: Business Communications | Business Energy
Back:My contact details and company details
Core products: Business Mobile • Telephony • Internet • Business Energy Solutions

Brand & Visual Direction
We have a group logo currently tailored more toward telecoms, plus a separate Varnek Energy logo.
Please explore layouts that use both logos or just one, whichever works best.
Color: I wouldn't mind seeing an option using our the Blue/Purple gradient from our website (varnek-example.co.uk), but also open to non-gradient approaches and other colours..

Overall look: Smart, modern, and distinctive.
Format & Print Specs
Double-sided business card format. (Use a standard size

Must-Haves
Front: Varnek wording or Varnek Group wording with atleast 1 logo also on front “Business Communications | Business Energy.”

Back: Contact + company details and core products.
A design that stands out while remaining professional.

Nice-to-Have Options
A gradient version using our site’s Blue/Purple gradient.
A non-gradient version.
A dual-logo treatment versus a single-logo treatment.

Thanks
Dominic

```html
<!DOCTYPE html>
<html lang="en">
<head>
<meta charset="utf-8">
<title>Varnek Group Business Card</title>
<link rel="stylesheet" href="https://fonts.googleapis.com/css2?family=Roboto:wght@400;500;700;900&display=swap">
<style>
  :root {
    --page: #ececec;
    --card: #ffffff;
    --navy: #231d6e;
    --blue: #1e6fd9;
    --blue-deep: #1657cf;
    --sky: #38b6e6;
    --green: #5cbf2a;
    --grey-text: #6f6f6f;
    --rule: #9a9a9a;
  }
  * { box-sizing: border-box; margin: 0; padding: 0; }
  html, body { width: 1200px; height: 900px; overflow: hidden; }
  body {
    background: var(--page);
    font-family: "Roboto", Arial, sans-serif;
    position: relative;
  }
  .card {
    position: absolute;
    width: 530px;
    height: 303px;
    background: var(--card);
    border-radius: 26px;
    overflow: hidden;
    box-shadow: 0 2px 8px rgba(0,0,0,.12);
  }
  .card--contact { left: 45px; top: 300px; }
  .card--products { left: 625px; top: 300px; }

  .brand {
    display: flex;
    align-items: center;
    gap: 10px;
  }
  .brand__name {
    font-weight: 900;
    color: var(--navy);
    letter-spacing: 1px;
    text-transform: uppercase;
  }
  .brand__dot {
    border-radius: 50%;
    flex-shrink: 0;
  }

  /* contact side */
  .card--contact .brand { position: absolute; left: 40px; top: 78px; }
  .card--contact .brand__name { font-size: 48px; }
  .card--contact .brand__dot { width: 34px; height: 34px; background: var(--sky); }
  .divider {
    position: absolute;
    left: 290px; top: 40px;
    width: 1px; height: 150px;
    background: var(--rule);
  }
  .contact { position: absolute; left: 310px; top: 44px; color: var(--grey-text); }
  .contact__name {
    color: var(--blue);
    font-weight: 500;
    font-size: 19px;
    text-transform: uppercase;
    letter-spacing: .5px;
  }
  .contact__role { font-size: 14px; margin-bottom: 8px; }
  .contact__address { font-size: 14px; line-height: 1.25; margin-bottom: 8px; }
  .contact__line {
    display: flex; align-items: center; gap: 6px;
    font-size: 14px; line-height: 1.4;
  }
  .contact__line svg { width: 11px; height: 11px; fill: var(--blue); flex-shrink: 0; }
  .descriptor-band {
    position: absolute;
    left: 0; right: 0; bottom: 36px;
    height: 42px;
    background: linear-gradient(90deg, var(--blue-deep), var(--sky));
    color: #fff;
    font-size: 16px;
    display: flex; align-items: center;
    padding-left: 40px;
  }

  /* products side */
  .card--products .brand {
    position: absolute; left: 0; right: 0; top: 88px;
    justify-content: center;
  }
  .card--products .brand__name { font-size: 58px; }
  .card--products .brand__dot { width: 40px; height: 40px; background: var(--green); }
  .products {
    position: absolute; left: 0; right: 0; top: 210px;
    display: flex; justify-content: center; gap: 10px;
    list-style: none;
    font-size: 13px; color: var(--grey-text);
  }
  .products li { display: flex; align-items: center; gap: 5px; }
  .products li::before {
    content: ""; width: 6px; height: 6px; border-radius: 50%;
    background: var(--green);
  }
</style>
</head>
<body>

<section class="card card--contact" aria-label="Business card, contact side">
  <div class="brand">
    <span class="brand__name">Varnek</span>
    <span class="brand__dot"></span>
  </div>
  <div class="divider"></div>
  <div class="contact">
    <p class="contact__name">Daniel Reeve</p>
    <p class="contact__role">Managing Director</p>
    <p class="contact__address">Your Address, City<br>State, Zip 0000</p>
    <p class="contact__line">
      <svg viewBox="0 0 24 24"><path d="M6.6 10.8a15 15 0 0 0 6.6 6.6l2.2-2.2a1 1 0 0 1 1-.25 11.4 11.4 0 0 0 3.6.6 1 1 0 0 1 1 1V20a1 1 0 0 1-1 1A17 17 0 0 1 3 4a1 1 0 0 1 1-1h3.5a1 1 0 0 1 1 1c0 1.25.2 2.45.6 3.6a1 1 0 0 1-.25 1z"/></svg>
      044-987 654 321
    </p>
    <p class="contact__line">
      <svg viewBox="0 0 24 24"><path d="M2 5h20v14H2zm2 2v.5l8 5 8-5V7z"/></svg>
      info@varnek-example.co.uk
    </p>
    <p class="contact__line">
      <svg viewBox="0 0 24 24"><circle cx="12" cy="12" r="10"/></svg>
      www.varnek-example.co.uk
    </p>
  </div>
  <div class="descriptor-band">Business Communications | Business Energy</div>
</section>

<section class="card card--products" aria-label="Business card, products side">
  <div class="brand">
    <span class="brand__name">Varnek</span>
    <span class="brand__dot"></span>
  </div>
  <ul class="products">
    <li>Business Mobile</li>
    <li>Telephony</li>
    <li>Internet</li>
    <li>Business Energy Solutions</li>
  </ul>
</section>

</body>
</html>
```